we are a small based family business that specialise in 12v led lights for tarvin caravans.
we also sell 12v switches, wire, circuit breakers, dimmers etc but our main line is LEDs.
We would like something that reflects the LED lighting on our cards.
www.reefcrestlamps.example.au is where you can have a look at to get ideas, of our product.
I have attached the logo we generally use on all our shopra listings and is the main header on our website.

Look forward to seeing what your team comes up with.

Business

Tam 0491 738 205
Corrawin Vale QLD 4391

www.reefcrestlamps.example

```html
<!DOCTYPE html>
<html lang="en">
<head>
<meta charset="utf-8">
<title>Reefcrest Lamps – Business Cards</title>
<link rel="stylesheet" href="https://fonts.googleapis.com/css2?family=Oswald:wght@400;700&family=Roboto+Condensed:wght@400&display=swap">
<style>
  :root {
    --bg: #e9e6e1;
    --card: #ffffff;
    --red: #b92a12;
    --black: #0d0d0d;
    --ink: #2a2a2a;
    --grey: #6b6b6b;
    --hatch: #c9c9c9;
  }
  * { box-sizing: border-box; margin: 0; padding: 0; }
  html, body { width: 1200px; height: 970px; overflow: hidden; background: var(--bg); }
  .canvas {
    width: 1200px; height: 970px;
    display: flex; flex-direction: column; align-items: center; justify-content: center; gap: 30px;
  }
  .card {
    position: relative; width: 780px; height: 446px;
    background: var(--card); overflow: hidden;
    box-shadow: 0 6px 18px rgba(0,0,0,.18);
  }
  .card svg.bands { position: absolute; inset: 0; }
  .wordmark {
    position: absolute; display: flex; align-items: center; gap: 12px;
    font-family: "Oswald", sans-serif; font-weight: 700; color: var(--black);
    text-transform: uppercase; letter-spacing: .5px; line-height: 1;
  }
  .wordmark .mark { width: 22px; height: 22px; background: var(--red); flex: none; }
  .front .wordmark { left: 360px; top: 120px; font-size: 46px; }
  .back .wordmark { left: 56px; top: 96px; font-size: 40px; }

  .person { position: absolute; left: 56px; top: 250px; }
  .person .name {
    font-family: "Oswald", sans-serif; font-weight: 400; font-size: 38px;
    color: var(--red); letter-spacing: 1px; text-transform: uppercase; line-height: 1.1;
  }
  .person .role {
    font-family: "Roboto Condensed", sans-serif; font-size: 19px;
    color: var(--grey); letter-spacing: 2px; text-transform: uppercase;
  }
  .divider { position: absolute; left: 362px; top: 178px; width: 3px; height: 150px; background: var(--red); }
  .contacts {
    position: absolute; left: 384px; top: 178px; list-style: none;
    font-family: "Roboto Condensed", sans-serif; font-size: 17px; color: var(--ink);
    display: flex; flex-direction: column; gap: 14px;
  }
  .contacts li { display: flex; align-items: center; gap: 10px; }
  .contacts svg { width: 22px; height: 22px; flex: none; }
  .hatch-edge {
    position: absolute; right: 0; top: 0; width: 22px; height: 100%;
    background: repeating-linear-gradient(135deg, var(--hatch) 0 1px, transparent 1px 5px);
  }
</style>
</head>
<body>
<main class="canvas">

  <section class="card front" aria-label="Card front">
    <svg class="bands" width="780" height="446" viewBox="0 0 780 446" aria-hidden="true">
      <polygon points="560,0 780,0 780,18 540,40" fill="var(--red)"/>
      <polygon points="0,300 780,190 780,290 0,400" fill="var(--red)"/>
      <polygon points="0,400 780,290 780,340 0,446" fill="var(--black)"/>
    </svg>
    <div class="wordmark"><span class="mark"></span>Reefcrest Lamps</div>
  </section>

  <section class="card back" aria-label="Card back">
    <svg class="bands" width="780" height="446" viewBox="0 0 780 446" aria-hidden="true">
      <polygon points="580,340 780,300 780,446 540,446" fill="var(--red)"/>
    </svg>
    <div class="hatch-edge"></div>
    <div class="wordmark"><span class="mark"></span>Reefcrest Lamps</div>

    <div class="person">
      <p class="name">Tam Harlow</p>
      <p class="role">General Manager</p>
    </div>

    <div class="divider"></div>
    <ul class="contacts">
      <li>
        <svg viewBox="0 0 22 22"><circle cx="11" cy="11" r="10" fill="none" stroke="var(--red)" stroke-width="1.6"/><path d="M8 6.5c-.8 2.8.9 6.5 4.6 8.6l1.6-1.6-2-1.2-.9.8c-1.2-.7-2.1-1.8-2.6-3l.9-.8-.9-2.2z" fill="var(--red)"/></svg>
        0491 738 205
      </li>
      <li>
        <svg viewBox="0 0 22 22"><circle cx="11" cy="11" r="10" fill="none" stroke="var(--red)" stroke-width="1.6"/><rect x="6.5" y="7.5" width="9" height="7" rx="1" fill="none" stroke="var(--red)" stroke-width="1.4"/><path d="M6.5 8l4.5 3.5L15.5 8" fill="none" stroke="var(--red)" stroke-width="1.4"/></svg>
        hello@reefcrestlamps.example
      </li>
      <li>
        <svg viewBox="0 0 22 22"><circle cx="11" cy="11" r="10" fill="none" stroke="var(--red)" stroke-width="1.6"/><circle cx="11" cy="11" r="5" fill="none" stroke="var(--red)" stroke-width="1.3"/><path d="M6 11h10M11 6c-2 3-2 7 0 10M11 6c2 3 2 7 0 10" fill="none" stroke="var(--red)" stroke-width="1"/></svg>
        www.reefcrestlamps.example
      </li>
      <li>
        <svg viewBox="0 0 22 22"><circle cx="11" cy="11" r="10" fill="none" stroke="var(--red)" stroke-width="1.6"/><path d="M11 16s-4-4.2-4-7a4 4 0 0 1 8 0c0 2.8-4 7-4 7z" fill="var(--red)"/><circle cx="11" cy="9" r="1.4" fill="#fff"/></svg>
        12 Harbour Lane, Corrawin Vale QLD 4391
      </li>
    </ul>
  </section>

</main>
</body>
</html>
```